Real Estate Valuation Services

format
A5 portrait, look at the picture
Double-sided: Front = visual & emotional, Back = informative & structured.
goal
Highlight the free hedonic property valuation as the main offer.
Build trust by presenting the company as an exclusive, family-owned real estate firm with local roots in Seewil/ZH.
Communicate the USP “Everything from one source” clearly – from valuation to notary support and tax guidance.
Target audience
Homeowners in the Lake Zurich region considering selling their property.
Clients who value exclusivity, professionalism, and personal service.
Design style
Modern, clean, elegant – plenty of white space. Look at the website: https://lindtaberhaus.ch/
Tone: Professional, trustworthy, exclusive – not like a mass-market flyer.
If possible, the text should be in German. Contact details must be included:
info@lindtaberhaus.ch
+41 77 586 12 47
Target Market(s)
property owner
Industry/Entity Type
real estate
Look and feel
Each slider illustrates characteristics of the customer's brand and the style your logo design should communicate.

```html
<!DOCTYPE html>
<html lang="de">
<head>
<meta charset="utf-8">
<title>Lindtaber Immobilien – Flyer A5</title>
<link rel="stylesheet" href="https://fonts.googleapis.com/css2?family=Montserrat:ital,wght@0,500;0,600;0,700;0,800;1,600&family=Lato:wght@400;700&display=swap">
<style>
  :root {
    --green-dark: #1f8a4c;
    --green: #2ea84f;
    --green-light: #7cc043;
    --ink: #1a1a1a;
    --text: #333333;
    --line: #9fcf6a;
    --bg: #f3f3f3;
    --paper: #ffffff;
  }
  * { box-sizing: border-box; margin: 0; padding: 0; }
  html, body { width: 1200px; height: 1137px; overflow: hidden; background: var(--bg); }
  body { position: relative; font-family: "Lato", Arial, sans-serif; color: var(--text); }

  .flyer {
    position: absolute; top: 204px; width: 520px; height: 738px;
    background: var(--paper); overflow: hidden;
  }
  .flyer--front { left: 65px; }
  .flyer--back { left: 614px; }
  .base-band { position: absolute; left: 0; right: 0; bottom: 0; height: 12px; background: var(--green-light); }

  /* Front */
  .front-headline {
    position: absolute; top: 48px; left: 0; right: 0; text-align: center;
    font-family: "Montserrat", Arial, sans-serif; font-weight: 800; font-size: 40px;
    line-height: 44px; color: var(--ink);
  }
  .front-quote {
    position: absolute; top: 157px; left: 0; right: 0; text-align: center;
    font-family: "Montserrat", Arial, sans-serif; font-style: italic; font-weight: 600;
    font-size: 20px; line-height: 28px; color: var(--green);
  }
  .front-rule { position: absolute; top: 225px; left: 109px; width: 284px; height: 2px; background: var(--line); }
  .front-scene {
    position: absolute; top: 290px; left: 0; right: 0; bottom: 12px;
    background: linear-gradient(180deg, #ffffff 0%, #d9dcdc 20%, #b9c2bd 45%, #8fb796 70%, #2f9a52 100%);
  }
  .front-portrait {
    position: absolute; left: 0; top: 300px; width: 300px; bottom: 12px;
    background: linear-gradient(180deg, #9c7458 0%, #b89a86 35%, #2a2a2a 70%, #1c1c1c 100%);
    border-radius: 150px 150px 0 0;
  }
  .front-brand {
    position: absolute; left: 306px; top: 618px; width: 196px; text-align: center;
    font-family: "Montserrat", Arial, sans-serif; font-weight: 600; color: #ffffff;
  }
  .front-brand .brand-name { display: block; font-size: 34px; line-height: 38px; }
  .front-brand .brand-sub { display: block; font-size: 17px; letter-spacing: 2px; line-height: 22px; }

  /* Back */
  .back-photo {
    position: absolute; top: 0; left: 0; right: 0; height: 213px;
    background: linear-gradient(180deg, #d8b98a 0%, #d8b98a 8%, #7fb6e6 9%, #aed2ef 38%, #4f8f7a 44%, #4a9bc2 52%, #2f8fb8 62%, #4d7d3e 74%, #c9a07a 88%, #e0d2c0 100%);
  }
  .offer-box {
    position: absolute; top: 204px; left: 27px; width: 468px; height: 177px;
    background: var(--paper); border: 2px solid var(--line); padding: 14px 28px 0;
  }
  .offer-title {
    text-align: center; font-family: "Montserrat", Arial, sans-serif; font-weight: 700;
    font-size: 19px; line-height: 23px; color: var(--green);
  }
  .offer-subtitle {
    text-align: center; font-family: "Montserrat", Arial, sans-serif; font-weight: 600;
    font-size: 18px; line-height: 22px; color: var(--green-dark);
  }
  .offer-rule { height: 1px; background: var(--line); margin: 9px 0 9px; }
  .offer-text { font-size: 14px; line-height: 19.5px; text-align: justify; color: var(--text); }

  .services { position: absolute; top: 403px; left: 30px; width: 462px; display: flex; justify-content: space-between; }
  .service {
    width: 146px; height: 151px; border: 2px solid var(--line); text-align: center;
    padding-top: 14px; background: var(--paper);
  }
  .service-icon { width: 40px; height: 40px; display: block; margin: 0 auto 6px; }
  .service-name { font-family: "Montserrat", Arial, sans-serif; font-weight: 700; font-size: 17px; color: var(--green); line-height: 22px; }
  .service-text { font-size: 13px; line-height: 16px; color: var(--text); margin-top: 2px; }

  .cta {
    position: absolute; top: 571px; left: 34px; width: 458px; height: 67px;
    background: linear-gradient(90deg, var(--green-dark) 0%, var(--green) 55%, var(--green-light) 100%);
    display: flex; align-items: center; justify-content: center; text-align: center;
    font-family: "Montserrat", Arial, sans-serif; font-weight: 700; font-size: 15px;
    line-height: 20px; color: #ffffff; letter-spacing: 0.3px;
  }

  .back-brand {
    position: absolute; left: 70px; top: 655px; width: 160px; text-align: center;
    font-family: "Montserrat", Arial, sans-serif; font-weight: 600; color: var(--green);
  }
  .back-brand .brand-name { display: block; font-size: 28px; line-height: 32px; }
  .back-brand .brand-sub { display: block; font-size: 14px; letter-spacing: 1.5px; line-height: 18px; }

  .contact { position: absolute; left: 263px; top: 657px; list-style: none; font-size: 13px; color: var(--text); }
  .contact li { display: flex; align-items: center; height: 17px; }
  .contact svg { width: 9px; height: 9px; margin-right: 7px; fill: var(--green-dark); }
</style>
</head>
<body>

<section class="flyer flyer--front" aria-label="Flyer Vorderseite">
  <h1 class="front-headline">Ihre Immobilie.<br>Unser Versprechen.</h1>
  <p class="front-quote">„Kostenlose und exklusive<br>Immobilienbewertung am Zürichsee.“</p>
  <div class="front-rule"></div>
  <div class="front-scene" role="img" aria-label="Landschaft am Zürichsee mit Bergen und Häusern"></div>
  <div class="front-portrait" role="img" aria-label="Porträt einer Immobilienberaterin"></div>
  <div class="front-brand">
    <span class="brand-name">Lindtaber</span>
    <span class="brand-sub">IMMOBILIEN</span>
  </div>
  <div class="base-band"></div>
</section>

<section class="flyer flyer--back" aria-label="Flyer Rückseite">
  <div class="back-photo" role="img" aria-label="Terrasse mit Pflanzen und Blick auf den Zürichsee"></div>

  <div class="offer-box">
    <h2 class="offer-title">Kostenlose Immobilienbewertung</h2>
    <p class="offer-subtitle">exklusiv für Eigentümer am Zürichsee</p>
    <div class="offer-rule"></div>
    <p class="offer-text">„Wir sind ein familiengeführtes Immobilienunternehmen aus Seewil. Mit persönlicher Betreuung und diskretem Service begleiten wir Sie – von der ersten Bewertung bis hin zu Notar- und Steuerfragen.“</p>
  </div>

  <div class="services">
    <div class="service">
      <svg class="service-icon" viewBox="0 0 40 40" fill="none" stroke="#1f8a4c" stroke-width="2.2" stroke-linejoin="round">
        <path d="M5 19 L19 7 L33 19"/><path d="M9 16 V33 H22"/><rect x="14" y="22" width="6" height="6"/>
        <circle cx="29" cy="29" r="7" stroke="#2ea84f"/><path d="M29 25 V33 M27 27 H31" stroke="#2ea84f" stroke-width="1.6"/>
      </svg>
      <div class="service-name">Bewertung</div>
      <div class="service-text">Marktgerechte<br>Wertermittlung</div>
    </div>
    <div class="service">
      <svg class="service-icon" viewBox="0 0 40 40" fill="none" stroke="#1f8a4c" stroke-width="2.2" stroke-linejoin="round" stroke-linecap="round">
        <rect x="16" y="4" width="16" height="10" rx="1" stroke="#2ea84f"/>
        <path d="M4 22 L12 18 L20 22 L28 18 L36 22"/><path d="M8 24 L16 31 L20 28 L24 31 L32 24"/><path d="M16 31 L14 34 M24 31 L26 34"/>
      </svg>
      <div class="service-name">Verkauf</div>
      <div class="service-text">Exklusive<br>Vermarktung<br>&amp; Beratung</div>
    </div>
    <div class="service">
      <svg class="service-icon" viewBox="0 0 40 40" fill="none" stroke="#1f8a4c" stroke-width="2.2" stroke-linejoin="round">
        <circle cx="20" cy="16" r="5"/>
        <path d="M20 5 V8 M20 24 V27 M9 16 H12 M28 16 H31 M12.5 8.5 L14.5 10.5 M25.5 21.5 L27.5 23.5 M27.5 8.5 L25.5 10.5 M14.5 21.5 L12.5 23.5"/>
        <path d="M4 34 L12 28 M36 34 L28 28" stroke="#2ea84f"/>
      </svg>
      <div class="service-name">Begleitung</div>
      <div class="service-text">Alles aus einer<br>Hand: Notar<br>&amp; Steuer</div>
    </div>
  </div>

  <div class="cta">„FORDERN SIE JETZT IHRE KOSTENLOSE<br>IMMOBILIENBEWERTUNG AN!“</div>

  <div class="back-brand">
    <span class="brand-name">Lindtaber</span>
    <span class="brand-sub">IMMOBILIEN</span>
  </div>

  <ul class="contact">
    <li><svg viewBox="0 0 10 10"><path d="M0 2 H10 V8 H0 Z M0 2 L5 5.5 L10 2" /></svg>info@lindtaberhaus.ch</li>
    <li><svg viewBox="0 0 10 10"><path d="M2 0 L4 2.5 L3 4 Q4.5 6.5 6 7 L7.5 6 L10 8 L8.5 10 Q2 9 0 1.5 Z"/></svg>+41 77 586 12 47</li>
    <li><svg viewBox="0 0 10 10"><circle cx="5" cy="5" r="5"/></svg>lindtaberhaus.ch</li>
  </ul>

  <div class="base-band"></div>
</section>

</body>
</html>
```